IT Services

We come to you
Only $49/hr
No contract, no monthly fee
Software engineer on staff
remote assistance or visit in your office

On the back of the card I want to list services.

- Server setup
- Network troubleshooting
- Printer setup
- Secure backup setup
- Software installation
- Wireless network setup
- Wired network setup
- Disaster recovery
- Website management
- Any other technology related support
- Email setup
- HIPAA compliance review and setup
Updates

the URL is: GEARFIXPRO.ZONE please use it on the card

On the card we need to mention "Connect remotely to address your IT issues" if there is enough room as well as "we go to you"

Industry/Entity Type

Printer

Contact Information for Business Card

I want a busoiness card to offer my services to doctor offices, it can be dentists, Otamatry, and other professions. I provide the following service. My plan is to go to their office and drop off my card. I don't want them to forget about it that is why I am paying for the design. I like hand writing design formats.

```html
<!DOCTYPE html>
<html lang="en">
<head>
<meta charset="utf-8">
<title>GearFixPro Business Card</title>
<link rel="stylesheet" href="https://fonts.googleapis.com/css2?family=Delius&family=Neucha&display=swap">
<style>
  :root {
    --page: #e9e7e4;
    --card: #ffffff;
    --navy: #2b2a86;
    --ink: #16163a;
    --slate: #3d3d6e;
    --green: #2e9a45;
    --band: #4a68b8;
    --link: #2f3f9c;
    --faint-blue: #dfe9f6;
    --faint-mix: #eef1ea;
  }
  * { box-sizing: border-box; margin: 0; padding: 0; }
  html, body {
    width: 1200px; height: 1200px; overflow: hidden;
    background: var(--page);
  }
  .canvas { position: relative; width: 1200px; height: 1200px; }

  .card {
    position: absolute; left: 125px; width: 955px;
    background: var(--card);
    overflow: hidden;
    box-shadow: 0 4px 14px rgba(0,0,0,0.18);
  }
  .card-front { top: 17px; height: 558px; }
  .card-back { top: 604px; height: 560px; }

  .backdrop-art { position: absolute; inset: 0; }
  .backdrop-front {
    background: radial-gradient(ellipse at 20% 30%, var(--faint-blue) 0%, rgba(255,255,255,0) 45%),
                radial-gradient(ellipse at 85% 40%, var(--faint-blue) 0%, rgba(255,255,255,0) 40%);
    opacity: 0.8;
  }
  .backdrop-back {
    left: 290px; top: 20px; width: 400px; height: 500px;
    background: radial-gradient(ellipse at 50% 55%, var(--faint-mix) 0%, var(--faint-blue) 35%, rgba(255,255,255,0) 70%);
    opacity: 0.7;
  }

  .front-text {
    position: absolute; left: 0; right: 0; text-align: center;
    font-family: "Delius", cursive;
  }
  .site-url { top: 22px; font-size: 86px; color: var(--navy); letter-spacing: 1px; }
  .site-url .tld { color: var(--green); }
  .headline { top: 137px; font-size: 66px; color: var(--ink); }
  .price { top: 216px; font-size: 50px; color: var(--ink); }
  .terms { top: 285px; font-size: 44px; color: #111; }
  .staff { top: 342px; font-size: 33px; color: var(--slate); line-height: 46px; }

  .contact-row {
    position: absolute; top: 452px; left: 0; right: 0;
    display: flex; justify-content: center; align-items: center; gap: 18px;
    font-family: "Delius", cursive; font-size: 29px;
  }
  .contact-name { color: #111; font-weight: 700; }
  .contact-divider { width: 2px; height: 40px; background: #333; }
  .contact-item { display: flex; align-items: center; gap: 8px; color: var(--link); }
  .contact-item svg { width: 28px; height: 28px; }

  .remote-band {
    position: absolute; left: 0; right: 0; bottom: 0; height: 57px;
    background: var(--band); color: #fff;
    font-family: "Delius", cursive; font-size: 25px;
    display: flex; align-items: center; justify-content: center;
  }

  .services-title {
    position: absolute; top: 30px; left: 0; right: 0; text-align: center;
    font-family: "Delius", cursive; font-size: 42px; color: #1a1a1a;
  }
  .service-list {
    position: absolute; top: 117px; list-style: none;
    font-family: "Neucha", cursive; font-size: 29px; color: #1d1d1d;
  }
  .service-list.col-left { left: 46px; }
  .service-list.col-right { left: 435px; }
  .service-list li {
    height: 59px; display: flex; align-items: center; gap: 14px;
  }
  .folder { width: 28px; height: 22px; flex: none; }
</style>
</head>
<body>
<div class="canvas">

  <section class="card card-front">
    <div class="backdrop-art backdrop-front" role="img" aria-label="Faint circuit board pattern background"></div>
    <div class="front-text site-url">www.gearfixpro<span class="tld">.zone</span></div>
    <div class="front-text headline">We come to you</div>
    <div class="front-text price">Only $49/hr</div>
    <div class="front-text terms">No contract, no monthly fee</div>
    <div class="front-text staff">Software engineer on staff<br>remote assistance or visit in your office</div>

    <div class="contact-row">
      <span class="contact-name">Dara Kellin</span>
      <span class="contact-divider"></span>
      <span class="contact-item">
        <svg viewBox="0 0 24 24" fill="none" stroke="#222" stroke-width="1.6" stroke-linecap="round" stroke-linejoin="round">
          <path d="M6 3l3 4-2 2c1 3 3 5 6 6l2-2 4 3-2 3C10 19 5 14 3 6z"/>
        </svg>
        1-800-555-0142
      </span>
      <span class="contact-divider"></span>
      <span class="contact-item">
        <svg viewBox="0 0 24 24" fill="none" stroke="#222" stroke-width="1.5">
          <circle cx="12" cy="12" r="9"/>
          <ellipse cx="12" cy="12" rx="4" ry="9"/>
          <line x1="3" y1="12" x2="21" y2="12"/>
          <line x1="5" y1="7" x2="19" y2="7"/>
          <line x1="5" y1="17" x2="19" y2="17"/>
        </svg>
        www.fixdeskhelp.com
      </span>
    </div>

    <div class="remote-band">Connect remotely to address your IT issues</div>
  </section>

  <section class="card card-back">
    <div class="backdrop-art backdrop-back" role="img" aria-label="Faint computer illustration in the background"></div>
    <h2 class="services-title">Our Service</h2>

    <svg width="0" height="0" style="position:absolute">
      <defs>
        <symbol id="folder-icon" viewBox="0 0 28 22">
          <path d="M2 4h8l2 3h14v13H2z" fill="none" stroke="#222" stroke-width="1.6" stroke-linejoin="round"/>
          <path d="M2 9h24" stroke="#222" stroke-width="1.2"/>
          <path d="M5 13l3 4M9 13l3 4M13 13l3 4" stroke="#222" stroke-width="1"/>
        </symbol>
      </defs>
    </svg>

    <ul class="service-list col-left">
      <li><svg class="folder"><use href="#folder-icon"/></svg>Server setup</li>
      <li><svg class="folder"><use href="#folder-icon"/></svg>Network troubleshooting</li>
      <li><svg class="folder"><use href="#folder-icon"/></svg>Printer setup</li>
      <li><svg class="folder"><use href="#folder-icon"/></svg>Secure backup setup</li>
      <li><svg class="folder"><use href="#folder-icon"/></svg>Software installation</li>
      <li><svg class="folder"><use href="#folder-icon"/></svg>Wireless network setup</li>
      <li><svg class="folder"><use href="#folder-icon"/></svg>Wired network setup</li>
    </ul>
    <ul class="service-list col-right">
      <li><svg class="folder"><use href="#folder-icon"/></svg>Disaster recovery</li>
      <li><svg class="folder"><use href="#folder-icon"/></svg>Website management</li>
      <li><svg class="folder"><use href="#folder-icon"/></svg>Any other technology related support</li>
      <li><svg class="folder"><use href="#folder-icon"/></svg>Email setup</li>
      <li><svg class="folder"><use href="#folder-icon"/></svg>HIPAA compliance review and setup</li>
    </ul>
  </section>

</div>
</body>
</html>
```